Mobile Recording Studio needs business cards

Open to seeing a creative design, but I want to emphasis my logo and minimize the name/title and company information. Possible a fully black background on card.

My company is a mobile sound recording studio. ok to include a my trailer (actual or cartoon) on the card. My initial thought is more straight forward, but a good design will win me over.

SPECS:
CMYK color mode
High (300ppi) raster effect.
cover bleed area
please deliver: Illustrator file with layers and a pdf at completion.

Name and info for the business card:

Mitchell Garvey
ADR Mixer

email: Mitchell@TakebayDub.example

address:
418 - 6057 East Pembury
Vancouver, BC V3R 2T4

phone:
604.419.8827 office

website:
www.TakebayDub.example

FB: @TakebayDub

Instagram: @TheTakebayDub

Industry/Entity Type

Television Production

Contact Information for Business Card

Mitchell Garvey
ADR Mixer

email: Mitchell@TakebayDub.example

address:
418 - 6057 East Pembury
Vancouver, BC V3R 2T4

phone:
604.419.8827 office

website:
www.TakebayDub.example

FB: @TakebayDub

Instagram: @TheTakebayDub

Colors

Designer to choose colors to be used in the design.

Requirements
Must have
• emphasis my logo and minimize the name/title and company information.
• SPECS:
• CMYK color mode
• High (300ppi) raster effect.
• cover bleed area
• please deliver: Illustrator file with layers and a pdf at completion.
Nice to have
• maybe include the following:
• all black background or black theme
• my work trailer (actual or cartoon) refer to Instagram: @TheTakebayDub

```html
<!DOCTYPE html>
<html lang="en">
<head>
<meta charset="utf-8">
<title>Takebay Dub – Business Cards</title>
<link href="https://fonts.googleapis.com/css2?family=Lato:wght@400;700&display=swap" rel="stylesheet">
<style>
  :root{
    --backdrop:#2a2a2b;
    --card:#1e1f21;
    --card-edge:#2c2d30;
    --silver:#d4d6d9;
    --grey-strong:#a9abae;
    --grey-soft:#7f8184;
    --rule:#5c5e61;
    --pattern-top:#242528;
    --pattern-bottom:#1c1d1f;
  }
  *{margin:0;padding:0;box-sizing:border-box}
  html,body{width:1200px;height:1108px;overflow:hidden;background:var(--backdrop)}
  body{font-family:"Lato",sans-serif;position:relative}
  .card{
    position:absolute;top:169px;width:440px;height:770px;
    background:var(--card);border-radius:24px;
    box-shadow:0 0 0 1px var(--card-edge);
    overflow:hidden;
  }
  .card--front{left:140px}
  .card--back{left:620px}

  .wordmark{color:var(--silver);font-weight:700;text-align:center;letter-spacing:1px}
  .card--front .wordmark{position:absolute;top:110px;left:0;right:0;font-size:62px;line-height:1.05}

  .contact{position:absolute;top:380px;left:0;right:0;text-align:center}
  .person__name{font-size:22px;font-weight:700;color:var(--grey-strong);text-transform:uppercase;letter-spacing:.5px}
  .person__role{font-size:17px;color:var(--grey-soft);margin-top:2px}
  .divider{width:300px;height:1px;background:var(--rule);margin:16px auto 20px}
  .phone{font-size:22px;color:var(--grey-strong);letter-spacing:1px}
  .email{font-size:18px;color:var(--grey-soft);margin-top:6px}
  .address{font-size:18px;color:var(--grey-soft);line-height:1.35;margin-top:6px}

  .pattern{position:absolute;inset:0;background:linear-gradient(180deg,var(--pattern-top),var(--pattern-bottom))}
  .card--back .wordmark{position:absolute;top:330px;left:0;right:0;font-size:40px}
  .socials{position:absolute;top:596px;left:0;right:0;display:flex;justify-content:center;gap:40px;font-size:18px;color:var(--grey-strong)}
  .social{display:flex;align-items:center;gap:8px}
  .social__dot{width:18px;height:18px;border-radius:50%;background:var(--grey-soft)}
  .website{position:absolute;top:644px;left:0;right:0;text-align:center;font-size:18px;color:var(--grey-soft)}
</style>
</head>
<body>
  <section class="card card--front">
    <div class="wordmark">Takebay<br>Dub</div>
    <div class="contact">
      <div class="person">
        <div class="person__name">Mitchell Garvey</div>
        <div class="person__role">ADR Mixer</div>
      </div>
      <div class="divider"></div>
      <div class="phone">604.419.8827</div>
      <div class="email">Mitchell@TakebayDub.example</div>
      <div class="address">418 - 6057 East Pembury<br>Vancouver, BC V3R 2T4</div>
    </div>
  </section>

  <section class="card card--back">
    <div class="pattern" role="img" aria-label="Faint repeated company wordmark texture"></div>
    <div class="wordmark">Takebay Dub</div>
    <div class="socials">
      <span class="social"><span class="social__dot"></span>@TakebayDub</span>
      <span class="social"><span class="social__dot"></span>@TheTakebayDub</span>
    </div>
    <div class="website">www.TakebayDub.example</div>
  </section>
</body>
</html>
```